Drowning Victims Recovery Website Design

We are working with Tidewell Search Dive Team. They provide recovery services for drowning victims so they can be reunited with their loved ones.

Some sites to use for inspiration:

https://shelterbrookvale.org
https://www.gallantascent.org
https://www.kindspringfund.org
https://www.tellano.ca/en

Thank you for taking the time to consider designing a website for us. We are web developers based in Stockton, CA, USA. Most of our projects go through the same process. Understanding this process may help you win a project with us. We custom-code all of our websites in-house. We don’t have any requirements as to what tools you use for your design, but we prefer Figma files. For any design that we label as four-stars, we send it to the client for review. The client picks the final design they want us to use. Once we complete this process, we will continue to show additional clients all the four-star sites and purchase them later. Your designs will have multiple chances to sell. For better chances of success, we ask that you follow these guidelines.

IMAGES:
If you use any images or icons in the design, we ask that you have a link to the asset so we can purchase the image/icon. Most of the designs we submit do not have the customer’s images on them unless they have some great images. Be creative; show us the feeling you are trying to portray with your image choices. Use any royalty-free site you choose. We subscribe to Quillmark and mainly use their images, but we can purchase images outside of Quillmark.

PLEASE NOTE: we will not submit designs to clients with watermarks on the images.

FONTS:
We ask that you identify the fonts used in the design. This can be done in a message if you want. We typically use Zintro Fonts and Quillmark Fonts.

CONTENT:
We're always open to different content and ideas. We often submit designs with stock images so the client can see our vision. We typically take pictures after the website launch to use their images with our vision. Lorem Ipsum is fine for paragraphs, but we ask that you write the headers in correct English. We want to be able to show the vision and identify the sections of the website.

INSPIRATION:
We typically add a couple of links in the brief of websites we like to help you get started in your design.

REVISIONS:
We do not often ask for revisions of the designs unless we see something in the design that may not appeal to the client. If there are slight changes that we want to make, we do that in the development process.

FEEDBACK:
We rarely give feedback on designs during the design process. We are working on many website projects and do not have the time to provide feedback. We usually respond if your request is well thought out and asks specific questions, but a note asking “feedback, please” usually goes unanswered.

```html
<!DOCTYPE html>
<html lang="en">
<head>
<meta charset="utf-8">
<title>Tidewell Search Dive Team</title>
<link href="https://fonts.googleapis.com/css2?family=Poppins:wght@400;500;600;700;800&display=swap" rel="stylesheet">
<style>
:root{
  --navy:#0f2b4a;
  --navy-deep:#0a1e35;
  --red:#b3121c;
  --red-dark:#8d0d15;
  --ink:#1c2b3c;
  --muted:#5e6873;
  --paper:#f1f2f4;
  --white:#ffffff;
}
*{box-sizing:border-box;margin:0;padding:0}
html,body{width:1200px;height:4624px;overflow:hidden}
body{font-family:'Poppins',sans-serif;color:var(--ink);background:var(--paper);position:relative}
.abs{position:absolute}
.pill{display:inline-block;border-radius:30px;font-weight:600;font-size:15px;letter-spacing:.3px;text-transform:uppercase;padding:12px 30px;text-decoration:none}
.pill-red{background:var(--red);color:var(--white)}
.pill-white{background:var(--white);color:var(--red)}
.pill-navy{background:var(--navy);color:var(--white);font-size:11px;padding:7px 16px}
.section-title{font-size:42px;font-weight:700;color:var(--navy);text-align:center;letter-spacing:.5px}
.section-title::after{content:"";display:block;width:70px;height:4px;background:var(--red);margin:10px auto 0;border-radius:2px}

/* header */
.site-header{top:0;left:0;width:1200px;height:180px;background:var(--white)}
.brand{left:40px;top:40px;display:flex;align-items:center;gap:14px}
.brand-mark{width:40px;height:40px;border-radius:50%;background:var(--red);flex:none}
.brand-name{font-size:28px;font-weight:800;color:var(--navy);line-height:1.05;width:240px}
.topbar{left:400px;top:0;width:800px;height:72px;background:var(--red);border-bottom-left-radius:40px;display:flex;align-items:center;gap:46px;padding-left:80px;color:var(--white);font-size:13px}
.topbar .item{display:flex;align-items:center;gap:10px}
.topbar .item b{display:block;font-size:14px}
.topbar .pill{margin-left:auto;margin-right:40px;background:var(--white);color:var(--red);padding:9px 22px;font-size:14px}
.main-nav{left:430px;top:100px;display:flex;gap:42px;font-size:16px;font-weight:500;color:var(--navy)}
.main-nav a{color:inherit;text-decoration:none;padding-bottom:6px}
.main-nav a.active{color:var(--red);border-bottom:3px solid var(--red)}

/* hero */
.hero{top:180px;left:0;width:1200px;height:720px;overflow:hidden}
.hero-photo{position:absolute;inset:0;background:radial-gradient(ellipse at 72% 35%,#2a6f9a 0%,#154067 38%,#0a2340 75%,#061628 100%)}
.hero-copy{left:112px;top:110px;color:var(--white)}
.hero-copy h1{font-size:56px;font-weight:700;line-height:1.1;letter-spacing:.5px}
.hero-copy p{font-size:17px;margin:22px 0 28px;width:440px;line-height:1.5;color:#dfe8f1}
.play{left:700px;top:260px;width:48px;height:48px;border-radius:50%;background:var(--white)}
.hero-curve{left:0;top:680px}

/* about */
.about{top:900px;left:0;width:1200px;height:320px;background:linear-gradient(180deg,#f4f5f7,#e9eaed)}
.about p{position:absolute;left:110px;top:60px;width:980px;text-align:center;font-size:15px;line-height:1.75;color:var(--muted)}
.about .read-more{position:absolute;left:522px;top:210px}
.about-title{top:852px;left:0;width:1200px}

/* services */
.services{top:1220px;left:0;width:1200px;height:1200px;background:linear-gradient(180deg,#10304f 0%,#1a4668 45%,#0d2744 100%)}
.services .section-title{color:var(--white);margin-top:72px}
.services .intro{text-align:center;color:#d6e1ec;font-size:16px;width:760px;margin:18px auto 0;line-height:1.6}
.card-grid{left:120px;top:240px;display:grid;grid-template-columns:repeat(3,300px);gap:24px 32px}
.service-card{background:var(--white);border-radius:12px;padding:18px;height:392px;display:flex;flex-direction:column;align-items:flex-start}
.service-card .photo{height:180px;width:100%;border-radius:8px;flex:none}
.service-card h3{font-size:18px;font-weight:700;color:var(--navy);margin:16px 0 6px;line-height:1.25}
.service-card p{font-size:13px;color:var(--muted);line-height:1.45;margin-bottom:12px}
.service-card .pill-navy{margin-top:auto}
.services .view-all{position:absolute;left:480px;top:1092px}

/* why */
.why{top:2420px;left:0;width:1200px;height:900px;background:var(--white)}
.why-photo{left:100px;top:100px;width:520px;height:540px;background:linear-gradient(160deg,#3f8fb3 0%,#1d5677 50%,#0b2b48 100%)}
.why-copy{left:648px;top:150px}
.why-copy h2{font-size:44px;font-weight:700;color:var(--navy)}
.why-copy ul{list-style:none;margin:24px 0 26px}
.why-copy li{display:flex;align-items:center;gap:14px;font-size:17px;font-weight:500;margin-bottom:10px;color:var(--ink)}
.tick{width:20px;height:20px;border-radius:50%;background:var(--red);flex:none}
.arrows{left:1024px;top:476px;display:flex;gap:10px}
.arrows span{width:26px;height:26px;border-radius:50%;border:2px solid var(--red)}
.arrows span.on{background:var(--red)}
.why-cards{left:132px;top:528px;display:flex;gap:16px}
.why-card{width:224px;height:252px;background:var(--white);border-radius:10px;box-shadow:0 6px 22px rgba(15,43,74,.16);text-align:center;padding:26px 16px 0}
.why-card .icon{width:70px;height:70px;border-radius:50%;background:var(--navy);margin:0 auto 14px;display:flex;align-items:center;justify-content:center}
.why-card.accent .icon{background:var(--red)}
.why-card h3{font-size:16px;font-weight:700;color:var(--navy);line-height:1.3;height:44px}
.why-card p{font-size:12px;color:var(--muted);line-height:1.5;margin:10px 0 10px}
.why-card a{font-size:13px;font-weight:600;color:var(--navy);text-decoration:none}

/* contact */
.contact{top:3320px;left:0;width:1200px;height:760px;background:linear-gradient(180deg,#eeeff2,#e6e7ea)}
.contact .section-title{margin-top:56px}
.contact .intro{text-align:center;font-size:16px;color:var(--muted);width:860px;margin:18px auto 0;line-height:1.6}
.form-box{left:100px;top:236px;width:1000px;height:440px;background:var(--white);box-shadow:0 8px 30px rgba(0,0,0,.1);padding:38px 60px}
.form-grid{display:grid;grid-template-columns:1fr 1fr;gap:24px 60px}
.field label{display:block;color:var(--red);font-size:15px;font-weight:500}
.field .line{border-bottom:1px solid #c9ccd1;font-size:13px;color:#8b929a;padding:8px 0}
.field.full{grid-column:1/3}
.field.full .line{height:64px}
.form-box .send{display:block;width:240px;margin:30px auto 0;text-align:center}

/* footer */
.footer-curve{top:4040px;left:0}
.site-footer{top:4130px;left:0;width:1200px;height:494px;background:linear-gradient(180deg,#0c2643,#081a30)}
.footer-brand{left:80px;top:70px;display:flex;align-items:center;gap:14px}
.footer-brand .brand-name{color:var(--white);font-size:24px;width:200px}
.footer-col{top:66px;color:#dfe6ee;font-size:15px}
.footer-col h4{color:var(--red);font-size:20px;font-weight:700;margin-bottom:18px;letter-spacing:.5px}
.footer-col li{list-style:none;margin-bottom:10px;display:flex;align-items:center;gap:10px}
.footer-col li::before{content:"";width:6px;height:6px;border-radius:50%;background:var(--red)}
.footer-col.contact-col li::before{display:none}
.dot-icon{width:24px;height:24px;border-radius:50%;background:var(--red);flex:none}
.bottom-bar{left:0;top:430px;width:1200px;height:64px;border-top:1px solid rgba(255,255,255,.15);display:flex;align-items:center;padding:0 110px;color:#c8d2dd;font-size:14px}
.socials{display:flex;gap:12px}
.socials span{width:28px;height:28px;border-radius:50%;background:var(--red)}
.bottom-bar .copy{margin-left:150px}
.bottom-bar .copy b{color:var(--red);font-weight:500}
</style>
</head>
<body>

<header class="abs site-header">
  <div class="abs brand"><span class="brand-mark"></span><span class="brand-name">Tidewell Search Dive Team</span></div>
  <div class="abs topbar">
    <div class="item"><svg width="22" height="22" viewBox="0 0 24 24"><path fill="#fff" d="M6.6 10.8a15 15 0 0 0 6.6 6.6l2.2-2.2a1 1 0 0 1 1-.25 11 11 0 0 0 3.6.6 1 1 0 0 1 1 1V20a1 1 0 0 1-1 1A17 17 0 0 1 3 4a1 1 0 0 1 1-1h3.5a1 1 0 0 1 1 1c0 1.25.2 2.45.57 3.57a1 1 0 0 1-.25 1z"/></svg><div><b>PHONE :</b>+1 555 014 2290</div></div>
    <div class="item"><svg width="22" height="18" viewBox="0 0 24 18"><rect x="1" y="1" width="22" height="16" rx="2" fill="none" stroke="#fff" stroke-width="2"/><path d="M1 2l11 8 11-8" fill="none" stroke="#fff" stroke-width="2"/></svg><div><b>MAIL :</b>dispatch@tidewellsearch.org</div></div>
    <a class="pill" href="#">Get in touch</a>
  </div>
  <nav class="abs main-nav">
    <a class="active" href="#">Home</a><a href="#">About Us</a><a href="#">Our Services</a><a href="#">Why Choose Us</a><a href="#">News</a><a href="#">Contact Us</a>
  </nav>
</header>

<section class="abs hero">
  <div class="hero-photo" role="img" aria-label="Scuba diver swimming through deep blue water"></div>
  <div class="abs hero-copy">
    <h1>EXPERT UNDERWATER<br>RECOVERY SERVICES</h1>
    <p>Safely recovering what matters most, with precision and dedication.</p>
    <a class="pill pill-white" href="#">Request a consultation</a>
  </div>
  <div class="abs play"><svg width="48" height="48" viewBox="0 0 48 48"><path d="M20 15l14 9-14 9z" fill="#b3121c"/></svg></div>
</section>

<svg class="abs hero-curve" width="1200" height="230" viewBox="0 0 1200 230" aria-hidden="true">
  <path d="M0 40 Q600 250 1200 40 L1200 230 L0 230 Z" fill="#f4f5f7"/>
  <path d="M0 20 Q600 240 1200 20" fill="none" stroke="#b3121c" stroke-width="14"/>
  <path d="M0 48 Q600 262 1200 48" fill="none" stroke="#0f2b4a" stroke-width="3"/>
</svg>

<section class="abs about">
  <p>Lorem ipsum dolor sit amet, consectetur adipiscing elit, sed do eiusmod tempor incididunt ut labore et dolore magna aliqua. Ut enim ad minim veniam, quis nostrud exercitation ullamco laboris nisi ut aliquip ex ea commodo consequat. Duis aute irure dolor in reprehenderit in voluptate velit esse cillum dolore eu fugiat nulla pariatur. Excepteur sint occaecat cupidatat non proident, sunt in culpa qui officia deserunt mollit anim id est laborum.</p>
  <a class="pill pill-red read-more" href="#">Read more</a>
</section>
<h2 class="abs about-title section-title">ABOUT INFORMATION</h2>

<section class="abs services">
  <h2 class="section-title">OUR SERVICES</h2>
  <p class="intro">It sounds like you're referring to organizations or teams that specialize in the recovery of individuals who have drowned, helping bring closure to families and loved ones.</p>
  <div class="abs card-grid">
    <article class="service-card"><div class="photo" role="img" aria-label="Search team on the water at sunset" style="background:linear-gradient(180deg,#e08a3a,#7a2f14)"></div><h3>Search and Recovery Operations:</h3><p>Conducting specialized search missions in bodies of water, including lakes, rivers.</p><a class="pill pill-navy" href="#">Learn more</a></article>
    <article class="service-card"><div class="photo" role="img" aria-label="Rescue crew working in the snow" style="background:linear-gradient(180deg,#dfe6ee,#8fa3b8)"></div><h3>Rescue Services:</h3><p>Swift response to drowning incidents in collaboration with emergency services.</p><a class="pill pill-navy" href="#">Learn more</a></article>
    <article class="service-card"><div class="photo" role="img" aria-label="Underwater drone inspecting the seabed" style="background:linear-gradient(180deg,#4f7a7a,#1f3a3e)"></div><h3>Underwater Drone/Robot Assistance:</h3><p>Using remotely operated vehicles (ROVs) or drones to assist in difficult-to-reach areas.</p><a class="pill pill-navy" href="#">Learn more</a></article>
    <article class="service-card"><div class="photo" role="img" aria-label="Blue underwater scene" style="background:linear-gradient(180deg,#6aa6d4,#1b3f73)"></div><h3>Body Recovery and Preservation:</h3><p>Employing proper techniques for preserving the body until it can be handed over.</p><a class="pill pill-navy" href="#">Learn more</a></article>
    <article class="service-card"><div class="photo" role="img" aria-label="Memorial candles and red roses" style="background:linear-gradient(180deg,#b8483e,#4a0f12)"></div><h3>Post-Recovery Services:</h3><p>Helping the family navigate the grieving process, offering emotional support.</p><a class="pill pill-navy" href="#">Learn more</a></article>
    <article class="service-card"><div class="photo" role="img" aria-label="Family comforting one another at home" style="background:linear-gradient(180deg,#c9a88a,#6b4a36)"></div><h3>Family Support and Notification:</h3><p>Providing a liaison between the family, authorities, and recovery teams to keep.</p><a class="pill pill-navy" href="#">Learn more</a></article>
  </div>
  <a class="pill pill-red view-all" href="#">View all services</a>
</section>

<section class="abs why">
  <div class="abs why-photo" role="img" aria-label="Divers descending through clear blue water"></div>
  <div class="abs why-copy">
    <h2>WHY CHOOSE US?</h2>
    <ul>
      <li><span class="tick"></span>Professional, certified divers</li>
      <li><span class="tick"></span>Advanced technology for sonar and underwater</li>
      <li><span class="tick"></span>Proven track record in recovery and safety</li>
      <li><span class="tick"></span>Available 24/7 for emergencies</li>
    </ul>
    <a class="pill pill-red" href="#">Meet our team</a>
  </div>
  <div class="abs arrows"><span></span><span class="on"></span></div>
  <div class="abs why-cards">
    <div class="why-card"><div class="icon"><svg width="34" height="34" viewBox="0 0 24 24"><path fill="#fff" d="M12 2l3 6 6 .9-4.5 4.3 1 6.3L12 16.5 6.5 19.5l1-6.3L3 8.9 9 8z"/></svg></div><h3>Expert Divers, Exceptional Results</h3><p>Lorem ipsum dolor sit amet, consectetur adipiscing elit.</p><a href="#">Learn More →</a></div>
    <div class="why-card"><div class="icon"><svg width="34" height="34" viewBox="0 0 24 24"><circle cx="12" cy="12" r="9" fill="none" stroke="#fff" stroke-width="2"/><path d="M12 7v5l3 3" stroke="#fff" stroke-width="2" fill="none"/></svg></div><h3>24/7 Availability for Emergency Recovery</h3><p>Lorem ipsum dolor sit amet, consectetur adipiscing elit.</p><a href="#">Learn More →</a></div>
    <div class="why-card accent"><div class="icon"><svg width="34" height="34" viewBox="0 0 24 24"><path d="M12 2l8 3v6c0 5-3.5 9-8 11-4.5-2-8-6-8-11V5z" fill="none" stroke="#fff" stroke-width="2"/><path d="M8 12l3 3 5-6" stroke="#fff" stroke-width="2" fill="none"/></svg></div><h3>Commitment to Safety and Quality</h3><p>Lorem ipsum dolor sit amet, consectetur adipiscing elit.</p><a href="#">Learn More →</a></div>
    <div class="why-card"><div class="icon"><svg width="34" height="34" viewBox="0 0 24 24"><circle cx="12" cy="12" r="9" fill="none" stroke="#fff" stroke-width="2"/><path d="M7.5 12l3 3 6-6" stroke="#fff" stroke-width="2" fill="none"/></svg></div><h3>Efficient, Thorough, and Reliable Service</h3><p>Lorem ipsum dolor sit amet, consectetur adipiscing elit.</p><a href="#">Learn More →</a></div>
  </div>
</section>

<section class="abs contact">
  <h2 class="section-title">GET IN TOUCH TODAY</h2>
  <p class="intro">Lorem ipsum dolor sit amet, consectetur adipiscing elit, sed do eiusmod tempor incididunt ut labore et dolore magna aliqua. Ut enim ad minim veniam.</p>
  <form class="abs form-box">
    <div class="form-grid">
      <div class="field"><label>First Name</label><div class="line">Lorem ipsum dolor</div></div>
      <div class="field"><label>Last Name</label><div class="line">Lorem ipsum dolor</div></div>
      <div class="field"><label>Phone</label><div class="line">Lorem ipsum dolor</div></div>
      <div class="field"><label>Email Address</label><div class="line">Lorem ipsum dolor</div></div>
      <div class="field full"><label>Message</label><div class="line">Lorem ipsum dolor</div></div>
    </div>
    <span class="pill pill-red send">Send your message</span>
  </form>
</section>

<svg class="abs footer-curve" width="1200" height="100" viewBox="0 0 1200 100" aria-hidden="true">
  <path d="M0 90 Q600 -40 1200 90 L1200 100 L0 100 Z" fill="#0c2643"/>
  <path d="M0 70 Q600 -60 1200 70" fill="none" stroke="#b3121c" stroke-width="12"/>
</svg>

<footer class="abs site-footer">
  <div class="abs footer-brand"><span class="brand-mark"></span><span class="brand-name">Tidewell Search Dive Team</span></div>
  <div class="abs footer-col" style="left:430px"><h4>USEFUL LINKS</h4><ul><li>Privacy policy</li><li>Terms of use</li><li>FAQ</li><li>Contact Us</li></ul></div>
  <div class="abs footer-col" style="left:680px"><h4>QUICK LINKS</h4><ul><li>Home</li><li>About Us</li><li>Our Services</li><li>Why Choose Us</li><li>News</li></ul></div>
  <div class="abs footer-col contact-col" style="left:912px"><h4>CONTACT US</h4><ul><li><span class="dot-icon"></span><span><b>PHONE :</b><br>+1 555 014 2290</span></li><li><span class="dot-icon"></span><span><b>MAIL :</b><br>dispatch@tidewellsearch.org</span></li></ul></div>
  <div class="abs bottom-bar">
    <div class="socials"><span></span><span></span><span></span><span></span></div>
    <div class="copy">© Copyrights 2025 <b>Tidewell Search Dive Team</b>. All Rights Reserved.</div>
  </div>
</footer>

</body>
</html>
```